Lantern Co. Supplement General Packaging Design

I am looking for a design template to design all of my various supplements and other products around. Meaning that this design should be able to just be able to change around words, up to a few small images, and text to suit my other various products.

The brand name is Lantern Co. and the slogan is: Legends Take Root
This is For an Apple Cider Vinegar Gummy, and include these top three things: Vegan, Gluten Free, Non-GMO somewhere in the design.

I want the design to have a luxurious feel. With some kind of design element where the logo is sort of the secondary aspect of the design.

Target Market(s)

Men age 24-45

Industry/Entity Type

Supplement

Requirements
Must have
• MUST HAVE A "vintage" LOOK AND FEEL. MUST HAVE ANOTHER design element besides the logo. (Something Vintage) MUST USE THE PROVIDED TEMPLATE A PDF IN THE FILES BELOW LABELED " TEMPLATE" and the LOGO PROVIDED under "Lantern Co. 2" OR "Lantern Co.3" whichever is better suited for the design. Bold design. Another color besides black to stand out. Use the lantern co logo which is below in the provided images. The design should go around the logo and fit the same aesthetic. The rest are for inspiration, what I like.

```html
<!DOCTYPE html>
<html lang="en">
<head>
<meta charset="utf-8">
<title>Lantern Co. Apple Cider Vinegar Gummy Label</title>
<link href="https://fonts.googleapis.com/css2?family=Archivo+Black&family=Arimo:wght@400;700&family=Montserrat:wght@500;600;700;800&family=Roboto+Slab:wght@700&display=swap" rel="stylesheet">
<style>
  :root{
    --stage:#bdbdbd;
    --red:#f11c0e;
    --orange:#f5821f;
    --black:#000;
    --white:#fff;
    --ink:#111;
  }
  *{box-sizing:border-box;margin:0;padding:0}
  html,body{width:1200px;height:904px;overflow:hidden;background:var(--stage)}
  body{position:relative;font-family:"Arimo",Arial,sans-serif;color:var(--ink)}

  .label{position:absolute;left:65px;width:1070px;height:367px;background:var(--red)}
  .label--white{top:47px}
  .label--orange{top:470px}

  .panel{position:absolute;top:13px;height:341px}
  .back-panel{left:0;width:393px;background:var(--white)}
  .facts-panel{left:677px;width:393px;background:var(--white)}
  .label--orange .back-panel,.label--orange .facts-panel{background:var(--orange)}
  .divider{position:absolute;left:393px;top:13px;width:7px;height:341px;background:var(--black)}

  /* back panel */
  .barcode-area{position:absolute;left:24px;top:80px;writing-mode:vertical-rl;font-family:"Montserrat",sans-serif;font-weight:800;font-size:20px;letter-spacing:.5px;color:var(--black)}
  .directions{position:absolute;left:85px;width:284px;font-size:10.9px;line-height:13px;letter-spacing:-.15px;text-align:justify}
  .directions b{font-weight:700}
  .use{top:21px}
  .caution{top:60px}
  .storage{top:124px;text-align:left}
  .allergen{top:163px}
  .disclaimer{position:absolute;left:85px;top:195px;width:284px;height:62px;border:1.5px solid var(--ink);padding:6px 7px;font-size:11.4px;line-height:14.5px;letter-spacing:-.15px;text-align:justify}
  .made-for-label{position:absolute;left:85px;top:263px;font-size:10.9px}
  .made-for-box{position:absolute;left:87px;top:285px;width:282px;height:40px;border:1.5px solid #333;background:var(--white);display:flex;align-items:center;justify-content:center;font-family:"Montserrat",sans-serif;font-weight:500;font-size:11.5px}

  /* claims column */
  .claims{position:absolute;left:400px;top:0;width:72px;height:367px;background:var(--orange);text-align:center;color:var(--black)}
  .claim{position:absolute;left:0;width:72px}
  .claim svg{display:block;margin:0 auto}
  .claim span{display:block;font-size:11.5px;line-height:13px;margin-top:5px}
  .claim--vegan{top:23px}
  .claim--gluten{top:97px}
  .claim--gmo{top:183px}
  .count{position:absolute;left:0;width:72px;top:295px;font-family:"Montserrat",sans-serif;font-weight:600;font-size:31px;line-height:34px;color:var(--white)}
  .count-unit{position:absolute;left:0;width:72px;top:329px;font-family:"Roboto Slab",serif;font-weight:700;font-size:12px;color:var(--black)}

  /* front panel */
  .front{position:absolute;left:472px;top:13px;width:205px;height:341px;background:var(--black);color:var(--white);text-align:center}
  .brand-mark{position:absolute;left:0;width:205px;top:38px}
  .brand-mark i{display:block;width:12px;height:12px;border:2px solid var(--white);border-radius:50%;margin:0 auto 4px}
  .est{position:absolute;left:0;width:205px;top:42px;font-family:"Montserrat",sans-serif;font-weight:600;font-size:6.5px;letter-spacing:1px;display:flex;justify-content:space-between;padding:0 61px}
  .brand-name{position:absolute;left:0;width:205px;top:63px;font-family:"Montserrat",sans-serif;font-weight:700;font-size:16px;letter-spacing:.5px}
  .tagline{position:absolute;left:0;width:205px;top:92px;font-family:"Montserrat",sans-serif;font-weight:600;font-size:6.5px;letter-spacing:1.3px}
  .product-name{position:absolute;left:0;width:205px;top:140px;font-family:"Montserrat",sans-serif;font-weight:800;font-size:32px;line-height:34px;letter-spacing:.3px}
  .category{position:absolute;left:0;width:205px;top:318px;font-family:"Montserrat",sans-serif;font-weight:600;font-size:9.5px;letter-spacing:2.3px}

  /* supplement facts */
  .facts{position:absolute;left:699px;top:35px;width:284px;height:306px;border:2.5px solid var(--black);padding:0 5px 0 7px;overflow:hidden}
  .facts h2{font-family:"Archivo Black",sans-serif;font-weight:400;font-size:22px;line-height:26px;text-align:center}
  .serving{font-weight:700;font-size:11.5px;line-height:14.5px;letter-spacing:.2px}
  .bar-thick{height:4.5px;background:var(--black);margin-top:4px}
  .facts-head{display:flex;justify-content:flex-end;gap:8px;font-weight:700;font-size:10.5px;line-height:13px;padding:2px 2px 1px 0;border-bottom:2px solid var(--black)}
  .row{display:grid;grid-template-columns:1fr 64px 30px;font-size:10.6px;line-height:13.6px;letter-spacing:-.1px;border-bottom:.8px solid #444;padding-top:.5px}
  .row .name{white-space:nowrap}
  .row .amt,.row .dv{text-align:right;white-space:nowrap}
  .row .dv{padding-right:1px}
  .row--indent1 .name{padding-left:10px}
  .row--indent2 .name{padding-left:17px}
  .row--tall{line-height:12.4px}
  .row--tall .amt,.row--tall .dv{align-self:start}
  .row:last-of-type{border-bottom:none}
  .facts-foot{border-top:5px solid var(--black);margin-top:1px;padding-top:2px;font-size:10.8px;line-height:13px}
  .facts-foot p{padding-left:3px}

  .ingredients{position:absolute;left:987px;top:29px;height:312px;writing-mode:vertical-rl;transform:rotate(180deg);font-size:10.6px;line-height:12.5px;width:52px}
  .ingredients b{font-weight:700}
</style>
</head>
<body>

<section class="label label--white">
  <div class="panel back-panel">
    <div class="barcode-area">BAR CODE AREA</div>
    <p class="directions use"><b>Suggested Use:</b> Take one (1) gummy daily or as directed by a healthcare professional.</p>
    <p class="directions caution"><b>Caution:</b> If you are pregnant, nursing, taking any medications or have any medical condition, consult your doctor before use. Discontinue use and consult your doctor if any adverse reactions occur.</p>
    <p class="directions storage">KEEP OUT OF REACH OF CHILDREN. STORE AT ROOM TEMPERATURE.</p>
    <p class="directions allergen">ALLERGEN WARNING: This product contains tree nuts (coconut).</p>
    <p class="disclaimer">†These statements have not been evaluated by the FDA. This product is not intended to diagnose, cure, treat or prevent any disease.</p>
    <p class="made-for-label">Manufactured for:</p>
    <div class="made-for-box">Manufactured for Meridian</div>
  </div>
  <div class="divider"></div>

  <div class="claims">
    <div class="claim claim--vegan">
      <svg width="38" height="38" viewBox="0 0 38 38"><circle cx="19" cy="19" r="17" fill="none" stroke="#000" stroke-width="2.4"/><path d="M18 27c-6 0-9-5-8-12 5 0 9 3 9 10zM20 27c0-8 3-12 9-13 0 7-3 12-9 13z" fill="#000"/></svg>
      <span>VEGAN</span>
    </div>
    <div class="claim claim--gluten">
      <svg width="38" height="38" viewBox="0 0 38 38"><circle cx="19" cy="19" r="17" fill="none" stroke="#000" stroke-width="2.4"/><g fill="#000"><ellipse cx="19" cy="10" rx="2" ry="3.5"/><ellipse cx="15.5" cy="15" rx="2" ry="3.5" transform="rotate(-30 15.5 15)"/><ellipse cx="22.5" cy="15" rx="2" ry="3.5" transform="rotate(30 22.5 15)"/><ellipse cx="15.5" cy="21" rx="2" ry="3.5" transform="rotate(-30 15.5 21)"/><ellipse cx="22.5" cy="21" rx="2" ry="3.5" transform="rotate(30 22.5 21)"/><rect x="18.2" y="22" width="1.6" height="9"/></g><line x1="7" y1="31" x2="31" y2="7" stroke="#000" stroke-width="2.4"/></svg>
      <span>GLUTEN<br>FREE</span>
    </div>
    <div class="claim claim--gmo">
      <svg width="38" height="38" viewBox="0 0 38 38"><circle cx="19" cy="19" r="17" fill="none" stroke="#000" stroke-width="2.4"/><text x="19" y="23" text-anchor="middle" font-family="Arial Black,Arial,sans-serif" font-weight="900" font-size="10" fill="#000">GMO</text><line x1="7" y1="31" x2="31" y2="7" stroke="#000" stroke-width="2.4"/></svg>
      <span>NON-GMO</span>
    </div>
    <div class="count">60</div>
    <div class="count-unit">Gummies</div>
  </div>

  <div class="front">
    <div class="brand-mark"><i></i></div>
    <div class="est"><span>EST.</span><span>2020</span></div>
    <div class="brand-name">LANTERN CO.</div>
    <div class="tagline">LEGENDS TAKE ROOT</div>
    <h1 class="product-name">APPLE<br>CIDER<br>VINEGAR<br>GUMMY</h1>
    <div class="category">DIETARY SUPPLEMENT</div>
  </div>

  <div class="panel facts-panel"></div>
  <div class="facts">
    <h2>Supplement Facts</h2>
    <p class="serving">Serving Size: &nbsp;1 Gummy<br>Servings Per Container: 60</p>
    <div class="bar-thick"></div>
    <div class="facts-head"><span>Amount Per Serving</span><span>% DV</span></div>
    <div class="row"><span class="name">Calories</span><span class="amt">10</span><span class="dv"></span></div>
    <div class="row"><span class="name">Total Carbohydrates</span><span class="amt">3 g</span><span class="dv">&lt;1%</span></div>
    <div class="row row--indent1"><span class="name">Total Sugars</span><span class="amt">2 g</span><span class="dv">**</span></div>
    <div class="row row--indent2"><span class="name">Includes 2 g Added Sugars</span><span class="amt"></span><span class="dv">4%</span></div>
    <div class="row"><span class="name">Vitamin B-6 (as Pyridoxine HCl)</span><span class="amt">0.5 mg</span><span class="dv">29%</span></div>
    <div class="row"><span class="name">Folate (120 mcg Folic Acid)</span><span class="amt">200 mcg DFE</span><span class="dv">50%</span></div>
    <div class="row"><span class="name">Vitamin B-12 (as Cyanocobalamin)</span><span class="amt">1.2 mcg</span><span class="dv">50%</span></div>
    <div class="row"><span class="name">Iodine (as Potassium Iodide)</span><span class="amt">50 mcg</span><span class="dv">33%</span></div>
    <div class="row row--tall"><span class="name">Apple Cider Vinegar Powder (fruit)<br>(providing 5% total acid)</span><span class="amt">500 mg</span><span class="dv">**</span></div>
    <div class="row"><span class="name">Pomegranate Juice Powder</span><span class="amt">40 mcg</span><span class="dv">**</span></div>
    <div class="row"><span class="name">Beet Root Juice Powder</span><span class="amt">40 mcg</span><span class="dv">**</span></div>
    <div class="facts-foot">
      <p>* % Daily Value Based on 2,000 Calorie Diet</p>
      <p>** Daily Value Not Established</p>
    </div>
  </div>
  <p class="ingredients"><b>Other Ingredients:</b> Glucose Syrup, Sugar, Glucose, Pectin, Sodium Citrate, Citric Acid, Natural Apple Flavor, Vegetable Oil, Liquid Apple Cider Vinegar, Purple carrot Juice Concentrate and Beta Carotene.</p>
</section>

<section class="label label--orange">
  <div class="panel back-panel">
    <div class="barcode-area">BAR CODE AREA</div>
    <p class="directions use"><b>Suggested Use:</b> Take one (1) gummy daily or as directed by a healthcare professional.</p>
    <p class="directions caution"><b>Caution:</b> If you are pregnant, nursing, taking any medications or have any medical condition, consult your doctor before use. Discontinue use and consult your doctor if any adverse reactions occur.</p>
    <p class="directions storage">KEEP OUT OF REACH OF CHILDREN. STORE AT ROOM TEMPERATURE.</p>
    <p class="directions allergen">ALLERGEN WARNING: This product contains tree nuts (coconut).</p>
    <p class="disclaimer">†These statements have not been evaluated by the FDA. This product is not intended to diagnose, cure, treat or prevent any disease.</p>
    <p class="made-for-label">Manufactured for:</p>
    <div class="made-for-box">Manufactured for Meridian</div>
  </div>
  <div class="divider"></div>

  <div class="claims">
    <div class="claim claim--vegan">
      <svg width="38" height="38" viewBox="0 0 38 38"><circle cx="19" cy="19" r="17" fill="none" stroke="#000" stroke-width="2.4"/><path d="M18 27c-6 0-9-5-8-12 5 0 9 3 9 10zM20 27c0-8 3-12 9-13 0 7-3 12-9 13z" fill="#000"/></svg>
      <span>VEGAN</span>
    </div>
    <div class="claim claim--gluten">
      <svg width="38" height="38" viewBox="0 0 38 38"><circle cx="19" cy="19" r="17" fill="none" stroke="#000" stroke-width="2.4"/><g fill="#000"><ellipse cx="19" cy="10" rx="2" ry="3.5"/><ellipse cx="15.5" cy="15" rx="2" ry="3.5" transform="rotate(-30 15.5 15)"/><ellipse cx="22.5" cy="15" rx="2" ry="3.5" transform="rotate(30 22.5 15)"/><ellipse cx="15.5" cy="21" rx="2" ry="3.5" transform="rotate(-30 15.5 21)"/><ellipse cx="22.5" cy="21" rx="2" ry="3.5" transform="rotate(30 22.5 21)"/><rect x="18.2" y="22" width="1.6" height="9"/></g><line x1="7" y1="31" x2="31" y2="7" stroke="#000" stroke-width="2.4"/></svg>
      <span>GLUTEN<br>FREE</span>
    </div>
    <div class="claim claim--gmo">
      <svg width="38" height="38" viewBox="0 0 38 38"><circle cx="19" cy="19" r="17" fill="none" stroke="#000" stroke-width="2.4"/><text x="19" y="23" text-anchor="middle" font-family="Arial Black,Arial,sans-serif" font-weight="900" font-size="10" fill="#000">GMO</text><line x1="7" y1="31" x2="31" y2="7" stroke="#000" stroke-width="2.4"/></svg>
      <span>NON-GMO</span>
    </div>
    <div class="count">60</div>
    <div class="count-unit">Gummies</div>
  </div>

  <div class="front">
    <div class="brand-mark"><i></i></div>
    <div class="est"><span>EST.</span><span>2020</span></div>
    <div class="brand-name">LANTERN CO.</div>
    <div class="tagline">LEGENDS TAKE ROOT</div>
    <h1 class="product-name">APPLE<br>CIDER<br>VINEGAR<br>GUMMY</h1>
    <div class="category">DIETARY SUPPLEMENT</div>
  </div>

  <div class="panel facts-panel"></div>
  <div class="facts">
    <h2>Supplement Facts</h2>
    <p class="serving">Serving Size: &nbsp;1 Gummy<br>Servings Per Container: 60</p>
    <div class="bar-thick"></div>
    <div class="facts-head"><span>Amount Per Serving</span><span>% DV</span></div>
    <div class="row"><span class="name">Calories</span><span class="amt">10</span><span class="dv"></span></div>
    <div class="row"><span class="name">Total Carbohydrates</span><span class="amt">3 g</span><span class="dv">&lt;1%</span></div>
    <div class="row row--indent1"><span class="name">Total Sugars</span><span class="amt">2 g</span><span class="dv">**</span></div>
    <div class="row row--indent2"><span class="name">Includes 2 g Added Sugars</span><span class="amt"></span><span class="dv">4%</span></div>
    <div class="row"><span class="name">Vitamin B-6 (as Pyridoxine HCl)</span><span class="amt">0.5 mg</span><span class="dv">29%</span></div>
    <div class="row"><span class="name">Folate (120 mcg Folic Acid)</span><span class="amt">200 mcg DFE</span><span class="dv">50%</span></div>
    <div class="row"><span class="name">Vitamin B-12 (as Cyanocobalamin)</span><span class="amt">1.2 mcg</span><span class="dv">50%</span></div>
    <div class="row"><span class="name">Iodine (as Potassium Iodide)</span><span class="amt">50 mcg</span><span class="dv">33%</span></div>
    <div class="row row--tall"><span class="name">Apple Cider Vinegar Powder (fruit)<br>(providing 5% total acid)</span><span class="amt">500 mg</span><span class="dv">**</span></div>
    <div class="row"><span class="name">Pomegranate Juice Powder</span><span class="amt">40 mcg</span><span class="dv">**</span></div>
    <div class="row"><span class="name">Beet Root Juice Powder</span><span class="amt">40 mcg</span><span class="dv">**</span></div>
    <div class="facts-foot">
      <p>* % Daily Value Based on 2,000 Calorie Diet</p>
      <p>** Daily Value Not Established</p>
    </div>
  </div>
  <p class="ingredients"><b>Other Ingredients:</b> Glucose Syrup, Sugar, Glucose, Pectin, Sodium Citrate, Citric Acid, Natural Apple Flavor, Vegetable Oil, Liquid Apple Cider Vinegar, Purple carrot Juice Concentrate and Beta Carotene.</p>
</section>

</body>
</html>
```